Masculine, visually appealing sales presentation for CPA firm

I have a basic power point that I use for sales presentations and I would like it to be updated to be more appealing and modern.

This is a presentation I give to real estate agents to help them close sales, save taxes, and resolve tax disputes. I would like the powerpoint to be updated to be more visually appealing. I have included the current powerpoint along with some of my logo files.

You don't have to use any of the pictures/clip art that is in the current power point. I only care that the words of the powerpoint make it to the new version.

Target Market(s)

Realtors, Real Estate Agents

Industry/Entity Type

Accounting

Requirements
Must have
• Visually appealing. I don't want it to look like I just took a template and made a normal powerpoint out of it. It should look custom.
Should not have
• Anything unprofessional, anything inconsistent with my brand

```html
<!DOCTYPE html>
<html lang="en">
<head>
<meta charset="utf-8">
<title>Taxation for Real Estate Professionals – Slide Deck</title>
<link href="https://fonts.googleapis.com/css2?family=Open+Sans:wght@400;600;700&display=swap" rel="stylesheet">
<style>
:root{
  --navy:#1d2b3f;
  --navy-deep:#142133;
  --brown:#3e2417;
  --paper:#ffffff;
  --band:#f2f2f2;
  --ink:#2a2a2a;
  --muted:#6d6d6d;
  --rule:#d9d9d9;
  --canvas:#ffffff;
}
*{box-sizing:border-box;margin:0;padding:0}
html,body{width:971px;height:1200px;overflow:hidden;background:var(--canvas)}
body{font-family:"Open Sans",Arial,sans-serif;color:var(--ink)}
.deck{display:grid;grid-template-columns:repeat(3,316px);grid-auto-rows:235px;gap:4px;padding:4px 8px;width:971px;height:1200px}
.slide{position:relative;overflow:hidden;background:var(--paper);box-shadow:0 0 0 1px #e3e3e3}
.brand{font-family:"Open Sans",Arial,sans-serif;font-weight:600;white-space:nowrap}
.brand-mini{position:absolute;top:10px;right:12px;font-size:7.5px;color:var(--navy);display:flex;align-items:center;gap:4px}
.brand-mini i{display:block;width:7px;height:7px;border-radius:50%;background:var(--navy)}
.head{position:absolute;left:0;top:0;right:0;height:28px;background:var(--band)}
.title{position:absolute;left:17px;top:8px;font-size:12.5px;font-weight:600;color:var(--ink);white-space:nowrap}
.title small{font-size:7px;font-weight:600}
.title::after{content:"";position:absolute;left:0;top:19px;width:32px;height:1.5px;background:var(--brown)}
.foot{position:absolute;left:0;right:0;bottom:0;height:11px;background:var(--navy-deep);font-size:4.2px;color:#cfd5de;padding:3px 0 0 6px}
.foot b{position:absolute;right:0;top:0;width:14px;height:11px;background:var(--brown)}
.foot em{position:absolute;right:18px;top:3px;font-style:normal}
.photo{position:absolute}
.dark{background:var(--navy)}
.dark .foot{background:transparent}
.cover-shade{position:absolute;inset:0;background:linear-gradient(120deg,#2a3a50,#1b283a 55%,#2e3d52)}
.cover-name{position:absolute;left:0;right:0;top:150px;text-align:center;color:#fff;font-size:26px}
.cover-dot{position:absolute;left:143px;top:70px;width:30px;height:30px;border-radius:50%;background:#fff}
.part{position:absolute;left:42px;top:88px;color:#fff}
.part .lbl{font-size:7px;position:absolute;left:0;top:0}
.part .num{font-size:28px;font-weight:600;position:absolute;left:0;top:7px;line-height:1}
.part .bar{position:absolute;left:22px;top:0;width:1px;height:60px;background:#9aa5b4}
.part .name{position:absolute;left:32px;top:20px;font-size:17px;white-space:nowrap;display:flex;align-items:center;gap:7px}
.tag{position:absolute;left:17px;top:186px;color:#fff;font-size:9.5px;line-height:1.35}
.divider-brand{position:absolute;right:15px;top:20px;color:#fff;font-size:10px;text-align:center}
.divider-brand i{display:block;width:22px;height:22px;border-radius:50%;background:#fff;margin:0 auto 5px}
.line{position:absolute;top:93px;left:0;right:0;height:1px;background:#bfbfbf}
.node{position:absolute;top:75px;width:36px;height:36px;border-radius:50%;color:#fff;font-size:6.5px;display:flex;align-items:center;justify-content:center}
.tick{position:absolute;top:93px;width:1px;height:14px;background:#bfbfbf}
.sect{position:absolute;top:110px;left:95px}
.sect .no{position:absolute;left:-20px;top:2px;width:14px;height:14px;color:#fff;font-size:7px;font-weight:700;display:flex;align-items:center;justify-content:center}
.sect h3{font-size:14px;font-weight:700;color:#222;white-space:nowrap}
.bul{list-style:none;font-size:7px;color:#555;line-height:14px;margin-top:2px}
.bul li::before{content:"• "}
.bul li.dash::before{content:"– "}
.items{position:absolute;font-size:7.3px;color:#555;line-height:1.3}
.item{display:flex;gap:10px;margin-bottom:13px}
.item svg{flex:none;width:12px;height:12px}
.tbl{position:absolute;font-size:7px;color:#444}
.tbl .r{display:flex;justify-content:space-between;padding:3px 4px;border-bottom:1px solid #eee}
.u{text-decoration:underline}
.sheet{position:absolute;background:#f6f6f6;font-size:5.3px;color:#555}
.sheet .r{display:flex;justify-content:space-between;padding:2px 6px;line-height:1.25}
.sheet .r:nth-child(odd){background:#ececec}
</style>
</head>
<body>
<main class="deck">

<section class="slide">
  <div class="photo cover-shade" role="img" aria-label="Muted office scene with people at work behind a navy overlay"></div>
  <div class="cover-dot"></div>
  <div class="cover-name brand">Hale Tax Advisory</div>
</section>

<section class="slide">
  <div class="photo" style="left:0;top:0;width:316px;height:140px;background:linear-gradient(135deg,#cfd3d8,#8d939c 60%,#4a5260)" role="img" aria-label="Business professionals shaking hands across a table"></div>
  <div style="position:absolute;left:0;top:140px;width:316px;height:46px;background:var(--navy);color:#fff;font-size:9.5px;text-align:center;padding-top:12px">Taxation for Real Estate Professionals©</div>
  <div style="position:absolute;left:20px;top:192px;font-size:5px;color:#888">Presented by:</div>
  <div style="position:absolute;left:20px;top:199px;font-size:8px;font-weight:700;color:var(--navy)">Owen Hale, CPA</div>
  <div style="position:absolute;left:30px;top:209px;font-size:4.5px;color:#999">Owner</div>
  <div style="position:absolute;left:219px;top:192px;font-size:5px;color:#888">Presentation to:</div>
  <div style="position:absolute;left:219px;top:199px;font-size:8px;font-weight:700;color:var(--navy)">Dana Whitfield</div>
  <div style="position:absolute;left:229px;top:209px;font-size:4.5px;color:#999">Vice President</div>
  <div class="foot" style="height:10px">© 2016 Hale Tax Advisory · Proprietary and Confidential. All rights reserved.<b style="width:48px;font-size:4px;color:#fff;padding:3px 2px 0;font-weight:700">September 26, 2016</b></div>
</section>

<section class="slide">
  <div style="position:absolute;left:141px;top:0;width:175px;height:235px;background:var(--navy)"></div>
  <div style="position:absolute;left:56px;top:84px;width:30px;height:30px;border-radius:50%;background:var(--navy)"></div>
  <div class="brand" style="position:absolute;left:0;width:141px;top:131px;text-align:center;font-size:11px;color:var(--navy)">Hale Tax Advisory</div>
  <div style="position:absolute;left:10px;width:121px;top:163px;text-align:center;font-size:5px;color:#777;line-height:1.3">4210 Alder Ridge Rd Ste 110,<br>Millbrook, OR 97031</div>
  <div style="position:absolute;left:141px;width:175px;top:44px;text-align:center;color:#fff;font-size:9.5px">Introductions</div>
  <div class="photo" style="left:190px;top:72px;width:76px;height:76px;border-radius:50%;border:3px solid #e6e6e6;background:linear-gradient(160deg,#8a7a6c,#4d4037)" role="img" aria-label="Portrait of the presenter"></div>
  <div style="position:absolute;left:141px;width:175px;top:157px;text-align:center;color:#fff;font-size:7px;font-weight:700">Owen Hale, CPA</div>
  <div style="position:absolute;left:141px;width:175px;top:168px;text-align:center;color:#dfe3e8;font-size:4.5px">Member of the National Guild of Tax Resolvers</div>
  <div style="position:absolute;left:90px;top:224px;font-size:4.5px;color:#555">National Guild of Tax Resolvers©</div>
</section>

<section class="slide">
  <div class="head"></div><div class="title">Table of Contents</div>
  <div class="brand-mini brand"><i></i>Hale Tax Advisory</div>
  <div class="line" style="left:40px"></div>
  <div class="node" style="left:41px;background:var(--navy)">Start</div>
  <div class="tick" style="left:101px"></div>
  <div class="sect"><span class="no" style="background:var(--brown)">1</span><h3>Taxation and Client</h3>
    <ul class="bul"><li>Sale of principal residence</li><li>Federal tax lien on real estate</li><li>Cancellation of debt</li></ul></div>
  <div class="foot">National Guild of Tax Resolvers©<em>4</em><b></b></div>
</section>

<section class="slide">
  <div class="head"></div><div class="title">Table of Contents</div>
  <div class="brand-mini brand"><i></i>Hale Tax Advisory</div>
  <div class="line"></div>
  <div class="tick" style="left:56px"></div>
  <div class="sect" style="left:70px"><span class="no" style="background:var(--brown)">2</span><h3>Taxation and the Realtor</h3></div>
  <ul class="bul" style="position:absolute;left:70px;top:129px"><li>Estimated taxes</li><li>Tax areas of special interest</li><li>Home office</li><li>Automobile</li></ul>
  <ul class="bul" style="position:absolute;left:198px;top:127px"><li>Employ children</li><li>Employ adult family</li><li>Family employees</li><li>Accounting Systems</li><li>$$$$$$$$$$$$$$</li></ul>
  <div class="foot">National Guild of Tax Resolvers©<em>5</em><b></b></div>
</section>

<section class="slide">
  <div class="head"></div><div class="title">Table of Contents</div>
  <div class="brand-mini brand"><i></i>Hale Tax Advisory</div>
  <div class="line" style="right:40px"></div>
  <div class="node" style="left:234px;background:var(--brown)">Finish</div>
  <div class="tick" style="left:53px"></div>
  <div class="sect" style="left:68px"><span class="no" style="background:var(--navy)">3</span><h3>Tax Problem Solutions</h3>
    <ul class="bul"><li>Unfiled returns</li><li>Ostrich method</li><li>If you owe money</li><li>How about audits?</li></ul></div>
  <div class="foot">National Guild of Tax Resolvers©<em>6</em><b></b></div>
</section>

<section class="slide dark">
  <div class="photo cover-shade" role="img" aria-label="Muted office scene behind a navy overlay"></div>
  <div class="divider-brand brand"><i></i>Hale Tax Advisory</div>
  <div class="part"><span class="lbl">Part</span><span class="num">1</span><span class="bar"></span>
    <span class="name"><svg width="11" height="13" viewBox="0 0 11 13"><rect x="0.5" y="0.5" width="10" height="12" fill="none" stroke="#fff"/><rect x="2" y="2" width="7" height="2.5" fill="#fff"/><g fill="#fff"><rect x="2" y="6" width="2" height="1.5"/><rect x="4.5" y="6" width="2" height="1.5"/><rect x="7" y="6" width="2" height="1.5"/><rect x="2" y="8.5" width="2" height="1.5"/><rect x="4.5" y="8.5" width="2" height="1.5"/><rect x="7" y="8.5" width="2" height="1.5"/></g></svg>Taxation and Your Client</span></div>
  <div class="tag">Closing controls commissions.<br>Liens control closings.</div>
  <div class="foot" style="bottom:5px">National Guild of Tax Resolvers©</div>
</section>

<section class="slide">
  <div class="head"></div><div class="title">Sale of Principal Residence</div>
  <div class="brand-mini brand"><i></i>Hale Tax Advisory</div>
  <div class="photo" style="left:14px;top:52px;width:131px;height:150px;background:linear-gradient(180deg,#9aa3aa,#8a7f72 55%,#6e7a5a)" role="img" aria-label="Stone two-storey house with a front lawn"></div>
  <div class="items" style="left:159px;top:62px;width:135px">
    <div class="item"><svg viewBox="0 0 12 12"><path d="M1 6 6 1.5 11 6M2.5 5v5.5h7V5" fill="none" stroke="#aaa" stroke-width="1.3"/></svg><span>Only one principal residence permitted.</span></div>
    <div class="item" style="margin-top:18px"><svg viewBox="0 0 12 12" fill="#aaa"><circle cx="4" cy="4" r="2"/><circle cx="8.5" cy="4.5" r="1.7"/><path d="M0.5 10c0-3 7-3 7 0zM6.5 10c0-2.5 5-2.5 5 0z"/></svg><span>Exclusion of $250,000 of gain, or $500,000 for married persons filing jointly.</span></div>
    <div class="item" style="margin-top:24px"><svg viewBox="0 0 12 12"><path d="M1 3h6M1 3v8h8V6M5 8l1-3 5-4.5 1 1L7 6z" fill="none" stroke="#aaa" stroke-width="1.1"/></svg><span>Must have been taxpayer's principal residence for 2 of the last 5 years.</span></div>
  </div>
  <div class="foot">National Guild of Tax Resolvers©<em>8</em><b></b></div>
</section>

<section class="slide">
  <div class="head"></div><div class="title">Federal Tax Lien on Real Estate</div>
  <div class="brand-mini brand"><i></i>Hale Tax Advisory</div>
  <svg style="position:absolute;left:0;top:88px" width="54" height="62" viewBox="0 0 54 62"><path d="M0 18h26V0l28 31-28 31V44H0z" fill="#8f9297"/><text x="14" y="29" font-size="3.6" fill="#fff" text-anchor="middle" font-family="Open Sans,sans-serif">Not applicable</text><text x="14" y="33" font-size="3.6" fill="#fff" text-anchor="middle" font-family="Open Sans,sans-serif">to principal</text><text x="14" y="37" font-size="3.6" fill="#fff" text-anchor="middle" font-family="Open Sans,sans-serif">residence</text></svg>
  <div style="position:absolute;left:78px;top:70px;width:210px;height:114px;background:#f6f6f6;border-radius:3px"></div>
  <div class="tbl" style="left:83px;top:75px;width:200px">
    <div class="r"><span>Selling price</span><span>$ 200,000</span></div>
    <div class="r" style="background:#efefef"><span>Less: Balance of PMM</span><span class="u">100,000</span></div>
    <div class="r"><span>Excess cash</span><span>$ 100,000</span></div>
    <div class="r" style="background:#efefef"><span>Current tax on sale</span><span class="u">20,000</span></div>
    <div class="r" style="background:#111;color:#fff;border:0"><span>Cash to IRS</span><span>$ 80,000*</span></div>
  </div>
  <div style="position:absolute;left:83px;top:167px;font-size:4.8px;color:#777">*apply to old tax liability, any excess would remain with taxpayer</div>
  <div class="foot">National Guild of Tax Resolvers©<em>9</em><b></b></div>
</section>

<section class="slide">
  <div class="head"></div><div class="title">Cancellation of Debt <small>(Short Sale)</small></div>
  <div class="brand-mini brand"><i></i>Hale Tax Advisory</div>
  <div class="photo" style="left:0;top:52px;width:100px;height:147px;background:linear-gradient(180deg,#b9ad9d,#d8cdbf 50%,#c46a70)" role="img" aria-label="Worried woman holding a wallet"></div>
  <div class="sheet" style="left:109px;top:54px;width:196px">
    <div class="r"><span>Amount of Debt Cancelled</span><span>$ &nbsp;&nbsp;&nbsp;&nbsp;100,000</span></div>
    <div class="r"><span>Less: FMV of Property</span><span>90,000</span></div>
    <div class="r"><span>Income from Cancellation of Debt</span><span>$ &nbsp;&nbsp;&nbsp;&nbsp;&nbsp;10,000</span></div>
    <div class="r"><span>&nbsp;</span><span></span></div>
    <div class="r"><span>Smaller of Debt Cancelled or FMV</span><span>$ &nbsp;&nbsp;&nbsp;&nbsp;&nbsp;90,000</span></div>
    <div class="r"><span>Less: Adjusted Basis</span><span>110,000</span></div>
    <div class="r"><span>Gain or (Loss)</span><span>$ &nbsp;&nbsp;&nbsp;&nbsp;(20,000)</span></div>
    <div class="r"><span>&nbsp;</span><span></span></div>
    <div class="r"><span>*$2M or less '07-'13</span><span></span></div>
    <div class="r"><span>**Non-deductible on person residence</span><span></span></div>
    <div class="r"><span>Exclusion from Gross Income:</span><span></span></div>
    <div class="r"><span>&nbsp;&nbsp;&nbsp;&nbsp;Bankruptcy or Insolvency</span><span></span></div>
  </div>
  <div class="foot">National Guild of Tax Resolvers©<em>10</em><b></b></div>
</section>

<section class="slide dark">
  <div class="photo cover-shade" role="img" aria-label="Muted office scene behind a navy overlay"></div>
  <div class="divider-brand brand"><i></i>Hale Tax Advisory</div>
  <div class="part"><span class="lbl">Part</span><span class="num">2</span><span class="bar"></span>
    <span class="name"><svg width="14" height="12" viewBox="0 0 14 12" fill="#fff"><rect x="0" y="8" width="2.5" height="3"/><rect x="3.5" y="6" width="2.5" height="5"/><rect x="7" y="3" width="2.5" height="8"/><rect x="10.5" y="0" width="2.5" height="11"/><rect x="0" y="11" width="14" height="1"/></svg>Taxes and the Realtor</span></div>
  <div class="tag">Taxes reduce profits.<br>Expenses reduce taxes.</div>
  <div class="foot" style="bottom:5px">National Guild of Tax Resolvers©</div>
</section>

<section class="slide">
  <div class="photo" style="left:0;top:0;width:158px;height:224px;background:linear-gradient(160deg,#6e7a5e,#7b6a55 50%,#3d3a3a)" role="img" aria-label="Figurine of a businessman carrying a stack of tax books"></div>
  <div class="brand-mini brand"><i></i>Hale Tax Advisory</div>
  <div class="title" style="left:170px;top:47px">Estimated Taxes</div>
  <div class="items" style="left:170px;top:80px;width:135px">
    <div class="item" style="margin-bottom:10px"><svg viewBox="0 0 12 12" fill="#aaa"><rect x="1" y="5" width="4" height="6"/><rect x="6" y="2" width="5" height="9"/></svg><span>Tax is due when income is earned.</span></div>
    <div class="item" style="margin-bottom:10px"><svg viewBox="0 0 12 12"><rect x="1" y="2" width="10" height="9" fill="none" stroke="#aaa"/><path d="M1 4.5h10" stroke="#aaa"/></svg><span>No magic to the 15th of April, June, September, or January.</span></div>
    <div class="item" style="margin-bottom:10px"><svg viewBox="0 0 12 12"><path d="M2 10 10 2M5 2h5v5" fill="none" stroke="#aaa" stroke-width="1.3"/></svg><span>Send in taxes only when you have money.</span></div>
    <div class="item"><svg viewBox="0 0 12 12"><path d="M1 3h6M1 3v8h8V6M5 8l1-3 5-4.5 1 1L7 6z" fill="none" stroke="#aaa" stroke-width="1.1"/></svg><span>We send in payments for many clients, at all different times.</span></div>
  </div>
  <div class="foot">National Guild of Tax Resolvers©<em>12</em><b></b></div>
</section>

<section class="slide">
  <div class="head"></div><div class="title">Documentation Issues</div>
  <div class="brand-mini brand"><i></i>Hale Tax Advisory</div>
  <div class="photo" style="left:0;top:62px;width:316px;height:130px;background:linear-gradient(90deg,#3c4654 0,#58606b 60%,#c9bda8 100%)" role="img" aria-label="Tax file folder and pen on a desk"></div>
  <div style="position:absolute;left:0;top:62px;width:208px;height:130px;background:rgba(29,43,63,.7);color:#fff;text-align:center;font-size:10.5px;line-height:1.4;padding-top:15px">“ IRS believes that taxpayers<br>are truthful and honest,<br><br style="line-height:4px">As long as it is<br>wrapped in proof! ”
    <div style="font-size:6.5px;margin-top:16px">More on this in Part 3 on audits...</div></div>
  <div class="foot">National Guild of Tax Resolvers©<em>13</em><b></b></div>
</section>

<section class="slide">
  <div class="head"></div><div class="title">Tax Areas of Special Interest</div>
  <div class="brand-mini brand"><i></i>Hale Tax Advisory</div>
  <div class="items" style="left:18px;top:58px;width:120px;font-size:6.8px">
    <div class="item" style="margin-bottom:12px"><svg viewBox="0 0 12 12"><rect x="1" y="1.5" width="10" height="9" fill="none" stroke="#aaa"/><path d="M3 4.5h6M3 6.5h6M3 8.5h6" stroke="#aaa"/></svg><span>The most audited:<br>Schedule C</span></div>
    <div class="item" style="margin-bottom:12px"><svg viewBox="0 0 12 12"><path d="M1 6 6 1.5 11 6M2.5 5v5.5h7V5" fill="none" stroke="#aaa" stroke-width="1.3"/></svg><span>Home office (8829)</span></div>
    <div class="item" style="margin-bottom:12px"><svg viewBox="0 0 12 12"><path d="M1 3h6M1 3v8h8V6M5 8l1-3 5-4.5 1 1L7 6z" fill="none" stroke="#aaa" stroke-width="1.1"/></svg><span>Auto expense (2106)<br>• Actual expenses<br>• Mileage method</span></div>
    <div class="item" style="margin-bottom:12px"><svg viewBox="0 0 12 12" fill="#aaa"><circle cx="4" cy="4" r="2"/><circle cx="8.5" cy="4.5" r="1.7"/><path d="M0.5 10c0-3 7-3 7 0zM6.5 10c0-2.5 5-2.5 5 0z"/></svg><span>Family employees</span></div>
    <div class="item"><svg viewBox="0 0 12 12"><rect x="1" y="1.5" width="10" height="7" fill="none" stroke="#aaa"/><path d="M4 10.5h4" stroke="#aaa"/></svg><span>Tracking expenses<br>• Computer, Logbooks<br>&nbsp;&nbsp;and Journals</span></div>
  </div>
  <div class="photo" style="left:141px;top:52px;width:50px;height:150px;background:linear-gradient(180deg,#e2dcd6,#c9c2bb)" role="img" aria-label="Laptop on a desk, left section"></div>
  <div class="photo" style="left:196px;top:52px;width:50px;height:150px;background:linear-gradient(180deg,#d8dde1,#9aa4ad)" role="img" aria-label="Laptop screen with spreadsheet, middle section"></div>
  <div class="photo" style="left:251px;top:52px;width:50px;height:150px;background:linear-gradient(180deg,#e6e1dc,#cfc8c0)" role="img" aria-label="Laptop on a desk, right section"></div>
  <div class="foot">National Guild of Tax Resolvers©<em>14</em><b></b></div>
</section>

<section class="slide">
  <div class="head"></div><div class="title">Home Office</div>
  <div class="brand-mini brand"><i></i>Hale Tax Advisory</div>
  <div class="photo" style="left:0;top:51px;width:113px;height:154px;background:linear-gradient(180deg,#b6c0c9,#8a5f4c 55%,#5d6a4c)" role="img" aria-label="Victorian brick house with a turret"></div>
  <div class="items" style="left:123px;top:56px;width:185px;font-size:6.5px;line-height:1.25">
    <div class="item" style="margin-bottom:6px"><svg viewBox="0 0 12 12"><rect x="1" y="1.5" width="10" height="9" fill="none" stroke="#aaa"/><path d="M3 4.5h6M3 6.5h6M3 8.5h6" stroke="#aaa"/></svg><b style="color:#222">Regular and exclusive use</b></div>
    <div class="item" style="margin-bottom:2px"><svg viewBox="0 0 12 12"><path d="M1 3h6M1 3v8h8V6M5 8l1-3 5-4.5 1 1L7 6z" fill="none" stroke="#aaa" stroke-width="1.1"/></svg><span><b style="color:#222">Indirect expenses</b> – must allocate, generally on square footage</span></div>
    <ul class="bul" style="margin-left:18px;font-size:6.5px;line-height:14px"><li>Mortgage interest &amp; property taxes</li><li>Homeowner's insurance</li><li>Repairs &amp; maintenance</li><li>Rent or depreciation (no land, 39 yrs.)</li><li>Utilities (may require different allocation %)</li><li>Water, sewer, trash, snow plowing, etc.</li><li>Lawn care/landscaping???</li><li class="dash">How aggressive are you?!?!</li></ul>
  </div>
  <div class="foot">National Guild of Tax Resolvers©<em>15</em><b></b></div>
</section>

</main>
</body>
</html>
```